Shaping Lattice Engineering

We need to design the look and feel for an innovation company with software products for solving complex IT problems following socio-technical theory thinking. The company is heavy in designing of complex systems (like an architect shop). The new design will form the foundation of our brand moving forward. We will approach software projects as if one is building a skyscraper or a bridge. We want to humanize technology and not the other way around. Our target groups will be healthcare and the environment. We will be able to take complex problems and turn them into amazing IT solutions that improve the quality of life for people.

Here are more fragments of ideas that can help:
===============

Motivation

The technology described in the application, coincides with “Steer-Via-Pulse” concept of Lorne Vistrup, which suggests managing a business by managing an informational representation of it : Lorne had the following vision:

"Imagine an enterprise design model that defines the behavior of an entire business. Imagine making this model a part of the corporate informational infrastructure, implementing it on technology that connects all relevant sources and users of information and affords maximum sharing among all parts of the firm. Managers could respond to the read-outs appearing on the console, modifying the flight plan en route based on changes in external conditions, monitoring the performance of delegated responsibilities, sending coordinated directions to subsidiary functions, and experiencing exhilaration upon their execution. It constitutes institutional memory and intelligence, which augment management's ability to run the business”.

This product does what Mr. Vistrup envisioned.

The Objective

QTV offers software products for the specification, construction, assembly, and ongoing management of a digital representation that is an exact mirror image of an enterprise. The main idea is the capability of managing the enterprise by managing an information technology representation of it through software. The idea is to manage the enterprise as a total system involving all aspects of operations. That makes the enterprise and all its information technology representation is inseparable. The implication is that the management of change at the business and IT infrastructure levels are unified. For example, by reconfiguring the information representation of the enterprise one can change business performance. By changing the configuration of the business representation one can actually change the organization’s ability to respond to internal and external events. Management leadership can act with the aid of technology to better respond and improve their ability to guide the organization. The knowledge management feature of the digital representation of the enterprise enables managers to monitor the impact of change and therefore help management assess risk and determine whether mitigating responses are necessary.

The technology and product defines a new approach for the design, implementation, and ongoing execution of software systems that are truly business-like rather than applications and workflows.

Software

```html
<!DOCTYPE html>
<html lang="en">
<head>
<meta charset="utf-8">
<title>Shaping Lattice Engineering</title>
<link rel="stylesheet" href="https://fonts.googleapis.com/css2?family=Open+Sans:wght@400;600;700&family=Raleway:wght@200;300&display=swap">
<style>
:root{
  --navy:#173c78;
  --navy-deep:#0c2a55;
  --blue:#1f72b8;
  --ink:#444b55;
  --muted:#8a9099;
  --line:#cfd3d8;
  --bar:#f1f1f1;
  --grey-band:#ececec;
  --sky:#d5e5f2;
  --white:#ffffff;
}
*{box-sizing:border-box;margin:0;padding:0}
html,body{width:1200px;height:2474px;overflow:hidden;background:var(--white)}
body{position:relative;font-family:"Open Sans",Arial,sans-serif;color:var(--ink)}
.abs{position:absolute}

/* top bar */
.topbar{left:0;top:0;width:1200px;height:40px;background:var(--bar)}
.social{left:141px;top:14px;display:flex;gap:14px}
.social span{width:11px;height:11px;border-radius:50%;background:#b3b7bc;display:block}
.search{left:412px;top:0;width:376px;height:40px;border-left:1px solid #e2e2e2;border-right:1px solid #e2e2e2;font-size:13px;color:#a5a9ae;padding:12px 14px}
.search svg{position:absolute;right:16px;top:13px}
.phone-top{left:940px;top:12px;font-size:13px;color:#9a9ea3;display:flex;gap:8px;align-items:center}

/* header */
.brand{left:141px;top:86px;display:flex;align-items:center;gap:10px;color:var(--navy);font-size:20px;font-weight:600;line-height:1;white-space:nowrap}
.brand .mark{width:14px;height:14px;background:var(--navy);display:block}
.nav{left:596px;top:90px;display:flex;font-size:13px;font-weight:700;color:var(--navy)}
.nav a{color:inherit;text-decoration:none;margin-right:40px}
.nav a:last-child{margin-right:0}
.nav .active{border-bottom:2px solid var(--navy);padding-bottom:3px}

/* hero */
.hero{left:0;top:40px;width:1200px;height:764px;background:linear-gradient(90deg,#f3f5f7 0%,#ffffff 45%,#ffffff 100%)}
.hero-title{left:138px;top:318px;font-family:"Raleway",sans-serif;font-weight:200;font-size:58px;line-height:66px;color:#3f444b}
.hero-copy{left:141px;top:466px;width:660px;font-size:14px;line-height:25px;color:var(--muted)}
.btn-outline{left:141px;top:571px;width:200px;height:46px;border:1px solid var(--line);display:flex;font-size:12px;letter-spacing:2px;color:#555;background:var(--white)}
.btn-outline .label{flex:1;display:flex;align-items:center;justify-content:center;border-right:1px solid var(--line)}
.btn-outline .arrow{width:46px;display:flex;align-items:center;justify-content:center}
.hero-visual{left:700px;top:96px;width:450px;height:700px;background:radial-gradient(ellipse at 50% 55%,#9fa5ad 0%,#c9ced4 40%,rgba(255,255,255,0) 72%)}

/* portfolio */
.portfolio{left:0;top:804px;width:1200px;height:396px;background:var(--grey-band)}
.section-title{width:1200px;left:0;text-align:center;color:var(--navy);font-size:29px;font-weight:400}
.section-title b{font-weight:700}
.section-sub{width:1200px;left:0;text-align:center;font-size:13px;color:#555}
.project{top:947px;width:455px;height:198px}
.project .pic{position:absolute;inset:0}
.project .btn-outline{left:0;top:152px;width:200px;height:46px}
.pager{top:1027px;width:38px;height:38px;background:var(--white);display:flex;align-items:center;justify-content:center}

/* what we do */
.what{left:0;top:1200px;width:1200px;height:445px;background:linear-gradient(180deg,#ffffff 0%,var(--sky) 100%)}
.what-copy{left:160px;top:1300px;width:880px;text-align:center;font-size:13px;line-height:20px;color:#555}
.what-visual{left:228px;top:1368px;width:290px;height:345px;background:radial-gradient(ellipse at 50% 50%,#6f7a88 0%,#a8b3c1 45%,rgba(213,229,242,0) 75%)}
.features{left:600px;top:1386px;list-style:none;font-size:15px;color:#555}
.features li{height:37.6px;display:flex;align-items:center;gap:14px}

/* clients */
.quote{font-family:Georgia,serif;font-size:110px;color:#d4d7db;line-height:1}
.client-copy{left:205px;top:1802px;width:790px;text-align:center;font-size:13px;line-height:21px;color:#666}
.client-name{left:0;width:1200px;top:1908px;text-align:center;font-size:13px;font-weight:700;color:var(--navy)}

/* contact */
.contact{left:0;top:1980px;width:1200px;height:425px;background:linear-gradient(180deg,#123666 0%,var(--navy-deep) 60%,#0a2247 100%)}
.contact-title{left:520px;top:2021px;width:160px;height:45px;display:flex;align-items:center;justify-content:center;color:var(--white);font-size:21px;font-weight:600;letter-spacing:.5px}
.contact-copy{left:141px;top:2110px;width:420px;font-size:14px;line-height:23px;color:var(--white)}
.contact-info{left:141px;top:2214px;list-style:none;font-size:12px;color:var(--white)}
.contact-info li{height:31px;display:flex;align-items:center;gap:14px}
.field{border:1px solid #4a6a96;background:rgba(10,30,65,.55);color:#c7d1de;font-size:13px;padding:14px 16px}
.send{left:618px;top:2316px;width:441px;height:44px;background:var(--blue);color:var(--white);font-size:14px;display:flex;align-items:center;justify-content:center}

.copyright{left:0;top:2428px;width:1200px;text-align:center;font-size:12px;color:#222}
</style>
</head>
<body>

<!-- Top bar -->
<div class="abs topbar"></div>
<div class="abs social" aria-hidden="true"><span></span><span></span><span></span><span></span><span></span></div>
<div class="abs search">Search
  <svg width="12" height="12" viewBox="0 0 12 12"><circle cx="5" cy="5" r="3.8" fill="none" stroke="#9a9ea3" stroke-width="1.4"/><line x1="8" y1="8" x2="11" y2="11" stroke="#9a9ea3" stroke-width="1.6"/></svg>
</div>
<div class="abs phone-top">
  <svg width="9" height="14" viewBox="0 0 9 14"><rect x=".7" y=".7" width="7.6" height="12.6" rx="1.5" fill="none" stroke="#9a9ea3" stroke-width="1.3"/><circle cx="4.5" cy="11" r=".9" fill="#9a9ea3"/></svg>
  4821 - 630 - 715
</div>

<!-- Hero -->
<section class="abs hero"></section>
<div class="abs brand"><span class="mark"></span>Shaping Lattice Engineering</div>
<nav class="abs nav">
  <a class="active">HOME</a><a>ABOUT US</a><a>SERVICES</a><a>PORTFOLIO</a><a>CONTACT US</a>
</nav>
<div class="abs hero-visual" role="img" aria-label="Photograph of a round high-rise tower under construction with exposed concrete floors and cranes"></div>
<h1 class="abs hero-title">Lorem ipsum dolor sit<br>amet consectetur piscing</h1>
<p class="abs hero-copy">Lorem ipsum dolor sit amet, consectetur adipiscing elit. Duis auctor erat eget lobortis dictum. Mauris dolor felis, rutrum quis elit ut, adipiscing accumsan nulla. Suspendisse neque velit, faucibus quis imperdiet a, blandit sit amet dolor.</p>
<div class="abs btn-outline"><span class="label">VIEW MORE</span><span class="arrow"><svg width="8" height="12" viewBox="0 0 8 12"><path d="M1.5 1l5 5-5 5" fill="none" stroke="#555" stroke-width="1.5"/></svg></span></div>

<!-- Portfolio -->
<section class="abs portfolio"></section>
<h2 class="abs section-title" style="top:848px">Latest <b>portfolio</b> projects</h2>
<p class="abs section-sub" style="top:893px">Lorem ipsum dolor sit amet, consectetur adipiscing elit. Nulla id congue mi, sed placerat</p>

<div class="abs pager" style="left:62px"><svg width="8" height="12" viewBox="0 0 8 12"><path d="M6.5 1l-5 5 5 5" fill="none" stroke="#777" stroke-width="1.5"/></svg></div>
<div class="abs pager" style="left:1089px"><svg width="8" height="12" viewBox="0 0 8 12"><path d="M1.5 1l5 5-5 5" fill="none" stroke="#777" stroke-width="1.5"/></svg></div>

<article class="abs project" style="left:129px">
  <div class="pic" role="img" aria-label="Wireframe drawing of a suspension bridge in rust orange on white" style="background:linear-gradient(180deg,#ffffff 0%,#f3e6de 55%,#e7d2c4 100%)"></div>
  <div class="abs btn-outline"><span class="label">VIEW PROJECT</span><span class="arrow"><svg width="8" height="12" viewBox="0 0 8 12"><path d="M1.5 1l5 5-5 5" fill="none" stroke="#555" stroke-width="1.5"/></svg></span></div>
</article>
<article class="abs project" style="left:604px">
  <div class="pic" role="img" aria-label="Upward view of blue glass skyscrapers against the sky" style="background:linear-gradient(160deg,#dbe9f6 0%,#6d9bcc 45%,#2d5f99 100%)"></div>
  <div class="abs btn-outline"><span class="label">VIEW PROJECT</span><span class="arrow"><svg width="8" height="12" viewBox="0 0 8 12"><path d="M1.5 1l5 5-5 5" fill="none" stroke="#555" stroke-width="1.5"/></svg></span></div>
</article>

<!-- What we do -->
<section class="abs what"></section>
<h2 class="abs section-title" style="top:1250px">What <b>we</b> do</h2>
<p class="abs what-copy">Lorem ipsum dolor sit amet, consectetur adipiscing elit. Duis ator erat eget lobortis dictum. Mauris dolor felis, rutrum Quis elit ut, adipiscing accumsan nulla. Suspendisse neque velit</p>
<div class="abs what-visual" role="img" aria-label="Photograph of a cylindrical tower under construction with blue glazing on the upper floors"></div>
<ul class="abs features">
  <li><svg width="7" height="10" viewBox="0 0 7 10"><path d="M1 1l4 4-4 4" fill="none" stroke="#555" stroke-width="1.4"/></svg>Lorem ipsum dolor sit amet.</li>
  <li><svg width="7" height="10" viewBox="0 0 7 10"><path d="M1 1l4 4-4 4" fill="none" stroke="#555" stroke-width="1.4"/></svg>consectetur adipiscing elit.</li>
  <li><svg width="7" height="10" viewBox="0 0 7 10"><path d="M1 1l4 4-4 4" fill="none" stroke="#555" stroke-width="1.4"/></svg>Duis auctor erat eget lobortis dictum.</li>
  <li><svg width="7" height="10" viewBox="0 0 7 10"><path d="M1 1l4 4-4 4" fill="none" stroke="#555" stroke-width="1.4"/></svg>Mauris dolor felis, rutrum, adipiscing accumsan nulla.</li>
  <li><svg width="7" height="10" viewBox="0 0 7 10"><path d="M1 1l4 4-4 4" fill="none" stroke="#555" stroke-width="1.4"/></svg>Suspendisse neque velit, faucibus quis imperdiet a.</li>
  <li><svg width="7" height="10" viewBox="0 0 7 10"><path d="M1 1l4 4-4 4" fill="none" stroke="#555" stroke-width="1.4"/></svg>blandit sit amet dolor.</li>
</ul>

<!-- Happy clients -->
<h2 class="abs section-title" style="top:1750px">Happy <b>clients</b></h2>
<div class="abs quote" style="left:150px;top:1795px">&ldquo;</div>
<div class="abs quote" style="left:998px;top:1865px">&rdquo;</div>
<p class="abs client-copy">Lorem ipsum dolor sit amet, consectetur adipiscing elit, sed do eiusmod tempor incididunt ut labore et dolore magna aliqua. Ut enim ad minim veniam, quis nostrud exercitation ullamco laboris nisi ut aliquip ex ea commodo consequat. Duis aute irure dolor in reprehenderit in voluptate velit esse cillum dolore eu fugiat nulla pariatur. Excepteur sint occaecat cupidatat non proident, sunt in culpa qui officia.</p>
<p class="abs client-name">- Client name here</p>

<!-- Contact -->
<section class="abs contact" role="img" aria-label="Night photograph of city high-rises in deep blue tones"></section>
<div class="abs contact-title">
  <svg class="abs" style="left:0;top:0" width="160" height="45" viewBox="0 0 160 45"><path d="M1 16V1h15M144 1h15v15M159 29v15h-15M16 44H1V29" fill="none" stroke="#3d8fd6" stroke-width="2"/></svg>
  CONTACT US
</div>
<p class="abs contact-copy">Lorem ipsum dolor sit amet, consectetur adipiscing elit. Duis auctor erat eget lobortis dictum. Mauris dolor felis, rutrum quis elit ut, adipiscing accumsan nulla. Suspendisse neque velit, faucibus quis imperdiet a, blandit sit amet dolor.</p>
<ul class="abs contact-info">
  <li><svg width="10" height="14" viewBox="0 0 10 14"><path d="M5 13.5S.8 8 .8 5a4.2 4.2 0 018.4 0c0 3-4.2 8.5-4.2 8.5z" fill="#fff"/><circle cx="5" cy="5" r="1.6" fill="#0c2a55"/></svg>88 Girder Lane, Harbor City, United States</li>
  <li><svg width="13" height="13" viewBox="0 0 13 13"><path d="M3 .8l2 3-1.3 1.5a8 8 0 004 4L9.2 8l3 2-1 2.2C6.5 12.5.5 6.5.8 1.8z" fill="#fff"/></svg>(4821) 630-715</li>
  <li><svg width="13" height="10" viewBox="0 0 13 10"><rect x=".5" y=".5" width="12" height="9" fill="#fff"/><path d="M.5 .5l6 5 6-5" fill="none" stroke="#0c2a55" stroke-width="1"/></svg>hello@shapinglattice.example</li>
</ul>
<div class="abs field" style="left:618px;top:2113px;width:211px;height:47px">Your Name..</div>
<div class="abs field" style="left:849px;top:2113px;width:210px;height:47px">Your email address..</div>
<div class="abs field" style="left:618px;top:2177px;width:441px;height:120px">Message..</div>
<div class="abs send">SEND MESSAGE</div>

<p class="abs copyright">© Copyright 2014 - Shaping Lattice Engineering. All rights reserved.</p>

</body>
</html>
```